Corrindale Planners, LLC Stationary

Corrindale Planners, LLC is a new financial planning and consulting company. We are looking for designs on business cards, letterhead, envelopes, and anything else that would be useful. Our preference for business card design is two sided. We are looking for a professional and clean look with incorporating the logo and patriotic feel. Thank you to all who participate and good luck!

```html
<!DOCTYPE html>
<html lang="en">
<head>
<meta charset="utf-8">
<title>Corrindale Planners, LLC Stationery</title>
<link href="https://fonts.googleapis.com/css2?family=Michroma&family=Exo+2:wght@400;600&display=swap" rel="stylesheet">
<style>
  :root {
    --backdrop: #e8e8e8;
    --paper: #f4f4f4;
    --navy: #0e355c;
    --red: #c0222b;
    --ink: #4a4a4a;
    --faint-navy: #dde0e4;
  }
  * { margin: 0; padding: 0; box-sizing: border-box; }
  html, body { width: 1200px; height: 821px; overflow: hidden; background: var(--backdrop); }
  .canvas { position: relative; width: 1200px; height: 821px; }

  .sheet { position: absolute; background: var(--paper); overflow: hidden; }

  .brand {
    display: flex; align-items: center; gap: 7px;
    font-family: "Michroma", sans-serif; color: var(--navy);
    text-transform: uppercase; white-space: nowrap;
  }
  .brand-dot { border-radius: 50%; background: var(--red); flex: none; }

  .faint-mark { position: absolute; border-radius: 50%; background: var(--faint-navy); }

  .small-text { font-family: "Exo 2", sans-serif; color: var(--ink); }

  /* Letterhead */
  .letterhead { left: 70px; top: 110px; width: 466px; height: 662px; }
  .letterhead .brand { position: absolute; top: 50px; left: 0; right: 0; justify-content: center; font-size: 14px; }
  .letterhead .brand-dot { width: 14px; height: 14px; }
  .letterhead .faint-mark { left: 60px; top: 200px; width: 346px; height: 346px; }
  .letterhead-footer { position: absolute; left: 0; right: 0; bottom: 22px; text-align: center; font-size: 7.5px; line-height: 12px; }
  .letterhead-footer b { color: var(--navy); font-weight: 600; }

  /* Envelope front */
  .envelope-front { left: 612px; top: 224px; width: 524px; height: 250px; }
  .envelope-front .brand { position: absolute; left: 26px; top: 34px; font-size: 11px; }
  .envelope-front .brand-dot { width: 11px; height: 11px; }
  .envelope-front .faint-mark { left: 270px; top: 20px; width: 226px; height: 226px; }
  .return-address { position: absolute; left: 23px; top: 210px; font-size: 7.5px; line-height: 10px; }

  /* Envelope back */
  .envelope-back { left: 618px; top: 514px; width: 524px; height: 248px; }
  .envelope-flap {
    position: absolute; left: 0; top: 0; width: 524px; height: 88px;
    background: var(--navy); border-radius: 0 0 12px 12px;
    display: flex; align-items: center; justify-content: center;
  }
  .envelope-flap .brand { color: var(--paper); font-size: 9px; }
  .envelope-flap .brand-dot { width: 9px; height: 9px; }
</style>
</head>
<body>
<main class="canvas">

  <section class="sheet letterhead" aria-label="Letterhead">
    <div class="brand"><span class="brand-dot"></span>Corrindale Planners, LLC</div>
    <div class="faint-mark" aria-hidden="true"></div>
    <footer class="letterhead-footer small-text">
      <div>412 Harlow Street, Brenton, Alaska 34501</div>
      <div><b>P :</b> 555 201 4470 &nbsp;<b>F :</b> 555 201 4471 &nbsp;<b>E :</b> hello@corrindale.com &nbsp;<b>W :</b> www.corrindale.com</div>
    </footer>
  </section>

  <section class="sheet envelope-front" aria-label="Envelope front">
    <div class="brand"><span class="brand-dot"></span>Corrindale Planners, LLC</div>
    <div class="faint-mark" aria-hidden="true"></div>
    <address class="return-address small-text" style="font-style:normal">
      412 Harlow Street<br>Brenton, Alaska 34501
    </address>
  </section>

  <section class="sheet envelope-back" aria-label="Envelope back">
    <div class="envelope-flap">
      <div class="brand"><span class="brand-dot"></span>Corrindale Planners, LLC</div>
    </div>
  </section>

</main>
</body>
</html>
```